Form Restoration Studio needs signs

We are looking to create three signs for our business. We need a 605 x 60 cm sign above the front door of the business and a smaller sign that is 153 x 90 cm. I have attached some basic ideas we have come up with but need something a lot more catchy.

Industry/Entity Type

Business

```html
<!DOCTYPE html>
<html lang="en">
<head>
<meta charset="utf-8">
<title>Form Restoration Studio – Sign Concepts</title>
<link rel="stylesheet" href="https://fonts.googleapis.com/css2?family=Cinzel:wght@500;600&family=Quicksand:wght@400;500&display=swap">
<style>
  :root {
    --plum: #6a2a8c;
    --plum-deep: #561c75;
    --plum-wave: #7a3a9c;
    --cream: #efefe8;
    --cream-shade: #e6e6dd;
    --band-text: #f4eef6;
    --page: #ffffff;
  }
  html, body { margin: 0; padding: 0; overflow: hidden; background: var(--page); }
  .canvas {
    position: relative; width: 1200px; height: 538px; overflow: hidden;
    background: var(--page);
    font-family: "Cinzel", "Times New Roman", serif; color: var(--plum);
  }
  .brand-name { position: absolute; font-weight: 600; white-space: nowrap; line-height: 1; margin: 0; }
  .brand-mark { position: absolute; border-radius: 50%; background: var(--plum); }
  .size-label {
    position: absolute; font-weight: 500; font-size: 19px; line-height: 26px; margin: 0;
  }

  /* master wordmark */
  .master .brand-mark { left: 66px; top: 150px; width: 44px; height: 44px; }
  .master .brand-name { left: 128px; top: 146px; font-size: 36px; text-align: center; line-height: 38px; }

  /* sign boards */
  .sign { position: absolute; background: var(--cream); overflow: hidden; }
  .sign-band { position: absolute; }
  .sign-band svg { display: block; width: 100%; height: 100%; }
  .services {
    position: absolute; margin: 0; padding: 0; list-style: none;
    font-family: "Quicksand", "Helvetica Neue", sans-serif; color: var(--band-text);
    white-space: nowrap; line-height: 1;
  }
  .services li { position: absolute; }
  .owner { position: absolute; font-weight: 500; white-space: nowrap; margin: 0; line-height: 1; }

  /* 153 x 90 board */
  .sign-square { left: 820px; top: 54px; width: 367px; height: 214px; }
  .sign-square .sheen { position: absolute; inset: 0; }
  .sign-square .brand-mark { left: 26px; top: 38px; width: 36px; height: 36px; }
  .sign-square .brand-name { left: 80px; top: 40px; width: 275px; font-size: 25px; line-height: 33px; text-align: center; }
  .sign-square .owner { left: 80px; width: 275px; text-align: center; top: 110px; font-size: 16px; }
  .sign-square .sign-band { left: 0; top: 150px; width: 367px; height: 64px; }
  .sign-square .services { left: 0; top: 150px; width: 367px; height: 64px; font-size: 24px; }

  /* 105 x 60 board */
  .sign-wide { left: 38px; top: 357px; width: 1150px; height: 114px; }
  .sign-wide .brand-mark { left: 30px; top: 24px; width: 36px; height: 36px; }
  .sign-wide .brand-name { left: 92px; top: 28px; font-size: 33px; }
  .sign-wide .owner { left: 92px; width: 490px; text-align: center; top: 76px; font-size: 21px; }
  .sign-wide .sign-band { left: 665px; top: 0; width: 485px; height: 114px; }
  .sign-wide .services { left: 665px; top: 0; width: 485px; height: 114px; font-size: 35px; }
</style>
</head>
<body>
<main class="canvas">

  <section class="master" aria-label="Primary wordmark">
    <span class="brand-mark" aria-hidden="true"></span>
    <h1 class="brand-name">Form Restoration<br>Studio</h1>
  </section>

  <p class="size-label" style="left:628px; top:148px;">Zice<br>153 x 90 cm.</p>
  <p class="size-label" style="left:40px; top:296px;">Zice<br>105 x 60 cm.</p>

  <section class="sign sign-square" aria-label="Sign 153 by 90 cm">
    <svg class="sheen" viewBox="0 0 367 214" preserveAspectRatio="none" aria-hidden="true">
      <path d="M0 120 C120 60 250 40 367 70 L367 0 L0 0 Z" fill="var(--cream-shade)" opacity="0.5"/>
    </svg>
    <span class="brand-mark" aria-hidden="true"></span>
    <h2 class="brand-name">Form Restoration<br>Studio</h2>
    <p class="owner">Miriam Hale R.M.T</p>
    <div class="sign-band" aria-hidden="true">
      <svg viewBox="0 0 367 64" preserveAspectRatio="none">
        <rect width="367" height="64" fill="var(--plum)"/>
        <path d="M0 34 C110 18 240 22 367 40 L367 64 L0 64 Z" fill="var(--plum-deep)"/>
      </svg>
    </div>
    <ul class="services">
      <li style="left:20px; top:6px;">Massage</li>
      <li style="left:157px; top:6px;">• Reiki</li>
      <li style="left:272px; top:6px;">• Sauna</li>
      <li style="left:38px; top:36px;">• Weight loss</li>
      <li style="left:196px; top:36px;">• Wellness</li>
    </ul>
  </section>

  <section class="sign sign-wide" aria-label="Sign 105 by 60 cm">
    <span class="brand-mark" aria-hidden="true"></span>
    <h2 class="brand-name">Form Restoration Studio</h2>
    <p class="owner">Miriam Hale R.M.T</p>
    <div class="sign-band" aria-hidden="true">
      <svg viewBox="0 0 485 114" preserveAspectRatio="none">
        <rect width="485" height="114" fill="var(--plum)"/>
        <path d="M0 66 C150 48 320 50 485 62 L485 114 L0 114 Z" fill="var(--plum-deep)"/>
      </svg>
    </div>
    <ul class="services">
      <li style="left:24px; top:14px;">• Massage • Reiki • Sauna</li>
      <li style="left:10px; top:64px;">Weight loss</li>
      <li style="left:258px; top:64px;">• Wellness</li>
    </ul>
  </section>

</main>
</body>
</html>
```